Etikett für ein Erfrischungsgetränk
Zielgruppe
Veltrano ist ein Startup Unternehmen, welches in naher Zukunft ein
Hibiskus-Erfrischungsgetränk auf den Markt bringen möchte.
Die Zielgruppe ist jedermann. Ob jung oder alt.
Aufgabenstellung
Das Etikett einer 0,33 l Longneckflasche soll:
Erfrischend, Modern aber auch Zeitlos, Einzigartig, dezent wirken.
Das Logo soll hervorstehen und der Hintergrund dezent sein.
Vorderetikett: 76 mm breit, 86 mm hoch
Rücketikett: 55 mm breit, 75 mm hoch
Die Getränkfarbe ist rötlich.

```html
<!DOCTYPE html>
<html lang="de">
<head>
<meta charset="utf-8">
<title>Veltrano – Etikett Erfrischungsgetränk</title>
<link rel="stylesheet" href="https://fonts.googleapis.com/css2?family=Amatic+SC:wght@700&family=Arimo:wght@400;700&display=swap">
<style>
  :root {
    --paper: #ffffff;
    --sun: #f7f36a;
    --blush: #f8c3df;
    --cyan: #5fe9f6;
    --teal: #5fdcc3;
    --brand: #b3147f;
    --ink: #111111;
    --petal: #ec5f80;
    --petal-deep: #c9304f;
  }
  html, body {
    margin: 0;
    padding: 0;
    overflow: hidden;
    background: var(--paper);
  }
  .label {
    position: relative;
    width: 1061px;
    height: 1200px;
    overflow: hidden;
    background: var(--paper);
  }
  .label__wash {
    position: absolute;
    inset: 0;
  }
  .label__brand {
    position: absolute;
    left: 0;
    width: 100%;
    top: 305px;
    margin: 0;
    text-align: center;
    font-family: "Arimo", sans-serif;
    font-weight: 700;
    font-size: 176px;
    line-height: 1;
    color: var(--brand);
    letter-spacing: -2px;
  }
  .label__product {
    position: absolute;
    left: 0;
    width: 100%;
    top: 655px;
    margin: 0;
    text-align: center;
    font-family: "Amatic SC", sans-serif;
    font-weight: 700;
    font-size: 68px;
    line-height: 1;
    color: var(--ink);
    letter-spacing: 1px;
    padding-left: 12px;
    box-sizing: border-box;
  }
  .label__sub {
    position: absolute;
    left: 0;
    width: 100%;
    top: 733px;
    margin: 0;
    text-align: center;
    font-family: "Arimo", sans-serif;
    font-weight: 400;
    font-size: 35px;
    line-height: 1;
    color: var(--ink);
    padding-left: 28px;
    box-sizing: border-box;
  }
  .label__flower {
    position: absolute;
    left: 400px;
    top: 800px;
    width: 230px;
    height: 230px;
  }
</style>
</head>
<body>
  <main class="label">
    <svg class="label__wash" viewBox="0 0 1061 1200" width="1061" height="1200" aria-hidden="true">
      <defs>
        <filter id="soft-edge" x="-10%" y="-10%" width="120%" height="120%">
          <feGaussianBlur stdDeviation="14"/>
        </filter>
        <linearGradient id="sun-band" x1="0" y1="0" x2="1" y2="0">
          <stop offset="0" stop-color="var(--sun)"/>
          <stop offset="0.5" stop-color="#fbe0c4"/>
          <stop offset="1" stop-color="#fbd9e9"/>
        </linearGradient>
        <linearGradient id="blush-band" x1="0" y1="0" x2="0" y2="1">
          <stop offset="0" stop-color="var(--blush)"/>
          <stop offset="0.6" stop-color="#fcd9ea"/>
          <stop offset="1" stop-color="#fdf2f7"/>
        </linearGradient>
        <linearGradient id="sea-band" x1="0" y1="0" x2="0" y2="1">
          <stop offset="0" stop-color="var(--cyan)"/>
          <stop offset="0.3" stop-color="#62e0ea"/>
          <stop offset="0.6" stop-color="var(--teal)"/>
          <stop offset="0.85" stop-color="#5ee3d9"/>
          <stop offset="1" stop-color="var(--cyan)"/>
        </linearGradient>
        <clipPath id="sun-clip">
          <rect x="0" y="0" width="1061" height="170"/>
        </clipPath>
      </defs>
      <circle cx="503" cy="520" r="480" fill="var(--sun)" clip-path="url(#sun-clip)"/>
      <rect x="0" y="150" width="1050" height="80" fill="url(#sun-band)" filter="url(#soft-edge)"/>
      <rect x="20" y="205" width="1030" height="390" fill="url(#blush-band)" filter="url(#soft-edge)"/>
      <rect x="0" y="615" width="1055" height="570" fill="url(#sea-band)" filter="url(#soft-edge)"/>
    </svg>

    <h1 class="label__brand">Veltrano</h1>
    <p class="label__product">Erfrischungsgetränk</p>
    <p class="label__sub">aus aufgebrühtem Hibiskustee</p>

    <svg class="label__flower" viewBox="0 0 230 230" role="img" aria-label="Illustration einer rosa Hibiskusblüte">
      <defs>
        <radialGradient id="bloom" cx="0.5" cy="0.5" r="0.5">
          <stop offset="0" stop-color="var(--petal-deep)"/>
          <stop offset="0.35" stop-color="var(--petal)"/>
          <stop offset="1" stop-color="#f28aa3"/>
        </radialGradient>
      </defs>
      <circle cx="115" cy="115" r="110" fill="url(#bloom)"/>
    </svg>
  </main>
</body>
</html>
```